Square graphic for social media post

I want to create a 1080 x 1080px all-black image for the quote below that I can share on social media. I want the emphasis to be primarily on the quote, secondarily on the portrait, and third (smallest) on the logo. I want the background on the portrait to be edited so it's transparent and just shows the face of the person on a black background (no brick wall visible).

Graphic color: black
Text color: white
Content: "What we went through is going to make the greatest generation of hoteliers our industry has ever seen." << biggest text
Derek Holloway << smaller text
President, Ridgemont Hotels << smaller text
[image of person - use whichever version looks better to you]
[Add Lodging Ledger logo - whichever looks better to you]

This image needs to be readable when sized down much smaller (400x400?) so want the text and portrait to take up most of the space.

I'd like the output both as PNG and original file (preferably Canva). Thanks!

Target Market(s)

Hotel managers

Industry/Entity Type

Hospitality

Font styles to use
Sans Serif

Colors

Designer to choose colors to be used in the design.

Requirements
Must have
• Needs to focus on the quote and the person quoted (the portrait)

```html
<!DOCTYPE html>
<html lang="en">
<head>
<meta charset="UTF-8">
<title>Derek Holloway Quote Card</title>
<link href="https://fonts.googleapis.com/css2?family=Figtree:wght@500;700;800&display=swap" rel="stylesheet">
<style>
  :root {
    --bg: #000000;
    --ink: #ffffff;
    --glow: #2a2a2a;
    --portrait-light: #8a8a8a;
    --portrait-mid: #4a4a4a;
    --portrait-dark: #111111;
  }
  html, body {
    margin: 0;
    padding: 0;
    background: var(--bg);
    overflow: hidden;
  }
  .card {
    position: relative;
    width: 1200px;
    height: 1200px;
    background: radial-gradient(circle at 52% 50%, var(--glow) 0%, var(--bg) 48%);
    overflow: hidden;
    font-family: "Figtree", "Helvetica Neue", Arial, sans-serif;
    color: var(--ink);
  }
  .portrait {
    position: absolute;
    left: 800px;
    top: 40px;
    width: 400px;
    height: 1160px;
    border-radius: 220px 0 0 0;
    background:
      radial-gradient(ellipse 70% 40% at 70% 45%, var(--portrait-light) 0%, var(--portrait-mid) 55%, transparent 80%),
      linear-gradient(180deg, var(--portrait-dark) 0%, var(--portrait-mid) 40%, var(--portrait-dark) 85%);
  }
  .masthead {
    position: absolute;
    left: 122px;
    top: 160px;
    width: 430px;
    display: flex;
    align-items: center;
    justify-content: center;
    gap: 16px;
    font-weight: 700;
    font-size: 34px;
    letter-spacing: 0.18em;
    text-transform: uppercase;
  }
  .masthead-dot {
    width: 14px;
    height: 14px;
    border-radius: 50%;
    background: var(--ink);
  }
  .quote {
    position: absolute;
    left: 123px;
    top: 366px;
    margin: 0;
    width: 640px;
    font-weight: 700;
    font-size: 57px;
    line-height: 70px;
    letter-spacing: -0.005em;
  }
  .attribution {
    position: absolute;
    left: 123px;
    top: 940px;
  }
  .attribution-name {
    margin: 0;
    font-weight: 500;
    font-size: 35px;
    letter-spacing: 0.05em;
    text-transform: uppercase;
  }
  .attribution-title {
    margin: 10px 0 0;
    font-weight: 500;
    font-size: 21px;
    letter-spacing: 0.05em;
    text-transform: uppercase;
  }
</style>
</head>
<body>
  <div class="card">
    <div class="portrait" role="img" aria-label="Black and white portrait of Derek Holloway, smiling, cropped at the right edge"></div>

    <div class="masthead">
      <span class="masthead-dot"></span>
      <span class="masthead-name">Lodging Ledger</span>
    </div>

    <p class="quote">"What we went<br>through is going to<br>make the greatest<br>generation of<br>hoteliers our<br>industry has ever<br>seen."</p>

    <div class="attribution">
      <p class="attribution-name">Derek Holloway</p>
      <p class="attribution-title">President, Ridgemont Hotels</p>
    </div>
  </div>
</body>
</html>
```